pet sitting business brochure

please create a professional bold brochure for my new pet sitting business
please use my logo and collect suitable photos online to go with design of brochure
my colour theme is orange and blue
please look at my website to collect information
www.kestrelpawminders.com.au

Reason: extended until tomorrow to make any changes to designs

```html
<!DOCTYPE html>
<html lang="en">
<head>
<meta charset="utf-8">
<title>Kestrel Paw Minders – Inside Spread</title>
<link rel="stylesheet" href="https://fonts.googleapis.com/css2?family=Arimo:wght@400;700&family=Roboto+Condensed:wght@700&display=swap">
<style>
  :root {
    --peach: #fde8d6;
    --sky: #cfe9f8;
    --mint: #ebf5ee;
    --orange: #f07f2a;
    --orange-head: #ef7d35;
    --blue: #1f88e8;
    --ink: #3a3a3a;
    --frame: #6f6f6f;
    --caption: #2b2b2b;
  }
  html, body {
    margin: 0;
    padding: 0;
    width: 1200px;
    height: 889px;
    overflow: hidden;
    background: #ffffff;
  }
  .canvas {
    position: relative;
    width: 1200px;
    height: 889px;
    background: #ffffff;
    font-family: "Arimo", Arial, sans-serif;
    color: var(--ink);
  }
  .spread {
    position: absolute;
    left: 33px;
    top: 24px;
    width: 1136px;
    height: 812px;
    display: flex;
    border: 1px solid var(--frame);
    box-sizing: border-box;
  }
  .panel {
    position: relative;
    width: 379px;
    height: 100%;
    overflow: hidden;
  }
  .panel + .panel { border-left: 1px solid var(--frame); }
  .panel--intro { background: var(--peach); }
  .panel--services { background: var(--sky); }
  .panel--extras { background: var(--mint); }
  .panel__art {
    position: absolute;
    left: 0;
    top: 0;
    width: 100%;
    height: 100%;
  }
  .intro__lead {
    position: absolute;
    left: 39px;
    top: 44px;
    width: 310px;
    margin: 0;
    font-weight: 700;
    font-size: 16px;
    line-height: 26px;
    color: var(--orange-head);
  }
  .intro__body {
    position: absolute;
    left: 36px;
    top: 198px;
    width: 310px;
    margin: 0;
    font-size: 13.4px;
    line-height: 22.8px;
    text-align: justify;
  }
  .section-title {
    margin: 0;
    font-family: "Roboto Condensed", "Arial Narrow", sans-serif;
    font-weight: 700;
    font-size: 22px;
    color: var(--orange-head);
  }
  .services {
    position: absolute;
    left: 30px;
    top: 374px;
    width: 322px;
    font-size: 13.4px;
    line-height: 22.8px;
  }
  .services .section-title { margin-bottom: 6px; }
  .services p { margin: 0 0 9.5px; }
  .services .service-name { font-weight: 700; }
  .services .service-copy { text-align: justify; }
  .extras {
    position: absolute;
    left: 36px;
    top: 33px;
    width: 320px;
    font-size: 13.4px;
    line-height: 22.8px;
  }
  .extras .section-title { margin-bottom: 10px; }
  .extras p { margin: 0 0 9.5px; }
  .extras strong { font-weight: 700; }
  .captions {
    position: absolute;
    left: 33px;
    top: 840px;
    width: 1136px;
    display: flex;
  }
  .captions span {
    width: 379px;
    text-align: center;
    font-family: "Arimo", Arial, sans-serif;
    font-size: 28px;
    color: var(--caption);
  }
</style>
</head>
<body>
<div class="canvas">
  <div class="spread">

    <section class="panel panel--intro">
      <svg class="panel__art" viewBox="0 0 379 812" aria-hidden="false">
        <ellipse cx="205" cy="652" rx="212" ry="232" fill="var(--blue)"/>
        <ellipse cx="218" cy="682" rx="205" ry="218" fill="url(#catTones)" role="img" aria-label="Photo of a woman hugging a ginger cat"/>
        <defs>
          <linearGradient id="catTones" x1="0" y1="0" x2="1" y2="1">
            <stop offset="0" stop-color="#c98a6a"/>
            <stop offset="0.5" stop-color="#e7b98a"/>
            <stop offset="1" stop-color="#f3e6dc"/>
          </linearGradient>
        </defs>
      </svg>
      <h2 class="intro__lead">Feel guilty that your dog is sitting at home alone all day long? While your away from home or at work? Let me spoil your pooch in your absence with a great&nbsp; ...</h2>
      <p class="intro__body">Kestrel Paw Minders offers a professional and caring pet sitting service to the Tarrow Valley. We will visit your home to care for your pet in the comfort of their own environment. We also offer a dog walking service for owners who are too busy or if you would like your dog exercised while you’re away from home to keep them entertained and happy. We care for all kinds of pets including horses, livestock, cats, dogs, rodents, birds, fish, and reptiles.</p>
    </section>

    <section class="panel panel--services">
      <svg class="panel__art" viewBox="0 0 379 812">
        <defs>
          <linearGradient id="horseTones" x1="0" y1="0" x2="1" y2="1">
            <stop offset="0" stop-color="#2a2320"/>
            <stop offset="0.55" stop-color="#6b5a48"/>
            <stop offset="1" stop-color="#d8c9a8"/>
          </linearGradient>
        </defs>
        <ellipse cx="190" cy="130" rx="196" ry="241" fill="var(--orange)"/>
        <ellipse cx="190" cy="120" rx="191" ry="227" fill="url(#horseTones)" role="img" aria-label="Photo of a young woman feeding hay to two dark horses at a fence"/>
      </svg>
      <div class="services">
        <h2 class="section-title">Services:</h2>
        <p class="service-name">Pet Sitting</p>
        <p>We come to your pet in your home. Includes:</p>
        <p>Feeding | Water checked | Play time</p>
        <p>Poop removal |&nbsp; Mail Collected | Bins taken in or out</p>
        <p class="service-name">Dog Walking</p>
        <p class="service-copy">Feel guilty that your dog is sitting at home alone all day long? While your away from home or at work? Let me spoil your pooch in your absence with a great dog walk!</p>
        <p class="service-copy">Professional Dog Walking is the core of all pet care. Daily dog walking provides a dog with a positive and healthy outlook towards its surroundings. Daily exercise helps to maintain or develop a dog's good temperament.</p>
      </div>
    </section>

    <section class="panel panel--extras">
      <svg class="panel__art" viewBox="0 0 379 812">
        <defs>
          <linearGradient id="walkTones" x1="0" y1="0" x2="0" y2="1">
            <stop offset="0" stop-color="#3f5a2e"/>
            <stop offset="0.6" stop-color="#6d7a3e"/>
            <stop offset="1" stop-color="#b89a72"/>
          </linearGradient>
        </defs>
        <ellipse cx="190" cy="472" rx="218" ry="247" fill="var(--blue)"/>
        <path d="M-20 480 A210 233 0 0 1 400 480 L400 812 L-20 812 Z" fill="url(#walkTones)" role="img" aria-label="Photo of a woman jogging along a forest path with a golden retriever"/>
      </svg>
      <div class="extras">
        <h2 class="section-title">Additional Services:</h2>
        <p><strong>Horses Rugged:</strong> Price charged on number of horses and ease of catching</p>
        <p><strong>Plants Watered:</strong> Price charged on number of plants and time spent.</p>
        <p><strong>Medicine Administered:</strong> charged daily</p>
      </div>
    </section>

  </div>
  <div class="captions">
    <span>inside page 2</span>
    <span>inside center page 3</span>
    <span>inside right page 4</span>
  </div>
</div>
</body>
</html>
```